Letterhead Design Project

Attached is our new Logo and a copy of our old letter head
Looking to rebrand with our new logo

Reason: I want to show a business card design

Industry/Entity Type

Film Production

Colors

Designer to choose colors to be used in the design.

Requirements
Must have
• The information on the old letterhead

```html
<!DOCTYPE html>
<html lang="en">
<head>
<meta charset="utf-8">
<title>Korva International Letterhead</title>
<link href="https://fonts.googleapis.com/css2?family=Arimo:ital,wght@0,400;0,700;1,400;1,700&display=swap" rel="stylesheet">
<style>
  :root {
    --teal: #01587a;
    --orange: #f58220;
    --brand-orange: #f26a1b;
    --grey: #8a8a8a;
    --white: #ffffff;
  }
  html, body {
    margin: 0;
    padding: 0;
    overflow: hidden;
    background: var(--white);
  }
  .letterhead {
    position: relative;
    width: 848px;
    height: 1200px;
    overflow: hidden;
    background: var(--white);
    font-family: "Arimo", Arial, sans-serif;
  }
  .header-feature {
    position: absolute;
    left: 0;
    top: 0;
    width: 660px;
    height: 190px;
    background: linear-gradient(100deg, var(--teal) 0%, var(--teal) 62%, var(--orange) 100%);
  }
  .contact {
    position: absolute;
    left: 102px;
    top: 40px;
    color: var(--white);
    font-style: italic;
  }
  .contact .tagline {
    font-size: 20px;
    font-weight: 700;
    margin: 0 0 10px;
  }
  .contact p {
    font-size: 14.5px;
    margin: 0;
    line-height: 19px;
  }
  .contact .indent { padding-left: 70px; }
  .contact .gap { margin-top: 4px; }
  .brand {
    position: absolute;
    right: 63px;
    top: 196px;
    display: flex;
    align-items: center;
    gap: 12px;
  }
  .brand-dot {
    width: 18px;
    height: 18px;
    border-radius: 50%;
    background: var(--orange);
  }
  .brand-name {
    font-size: 46px;
    font-weight: 700;
    color: var(--teal);
    letter-spacing: 2px;
  }
  .footer {
    position: absolute;
    left: 0;
    right: 0;
    top: 1085px;
    text-align: center;
    color: var(--teal);
    font-size: 13.5px;
    line-height: 17.5px;
  }
  .footer p { margin: 0; }
  .footer .mark { color: var(--brand-orange); font-weight: 700; }
  .footer .bullet { color: var(--brand-orange); }
  .footer .small { font-size: 12px; }
  .footer .company { font-weight: 700; }
  .footer .registration { color: var(--grey); }
</style>
</head>
<body>
<div class="letterhead">
  <div class="header-feature" role="img" aria-label="Decorative teal and orange header graphic"></div>

  <div class="contact">
    <p class="tagline">Supply &amp; Management of Infrastructure and Logistics</p>
    <p>P.O. Box: 482 Millbrook QLD 4309</p>
    <p class="indent">76 Harlow NSW 2175</p>
    <p class="gap">Ph. 0400 000 123</p>
    <p class="gap">Email: hello@korva.com.au</p>
  </div>

  <div class="brand">
    <span class="brand-dot"></span>
    <span class="brand-name">KORVA</span>
  </div>

  <div class="footer">
    <p><span class="bullet">●</span> <span class="mark">KORVA</span> Film Services<span class="bullet">●</span><span class="mark">KORVA</span> Pilot Escorts<span class="bullet">●</span><span class="mark">KORVA</span> Tour Management <span class="bullet">●</span></p>
    <p><span class="bullet">●</span><span class="mark">KORVA</span> Driver<span class="bullet">●</span></p>
    <p><span class="small">are divisions of</span> <span class="mark">KORVA</span> <span class="company">International Pty Ltd</span></p>
    <p class="registration">ACN 000 111 222 ABN 00 000 111 222</p>
  </div>
</div>
</body>
</html>
```